The Bright Meadow Foundation

This is a non profit . We are a 501(c)(3) charitable organization in the United States. The organization is a volunteer based group providing basic healthcare to those living in underserved rural areas around the world. I have attached a brochure that provides some information about the organization. We are looking for a basic 5 page web page Page 1 Photos that fade into the next x 3 with mission statementPage 2 About us - details about bright meadow foundation. also introducing our Founders of the organization. Marina Kellet, M.D. Dorla Penn , FNP, Rosa Tembley, FNP, Wade Marlow. ( will provide you info on each.Page 3 Projects coming up and futurePage 4 Get involved - Give a donation, Volunteer, Corporate supportPage 5 Support us and contact us with a message box.We mainly work in South America but anticipate trave to South Africa in the near future. Colors bright with emphasis on Reds and Purples. I have attached some photos and ideas. You can use or not use ok to use something similar if you so like

Target Market(s)

People interested in volunteering time or money to overseas medical work. NOT a religious base

Coding

Coded - Design and coding required

Number of Pages Required

1 page

Colors
876aae
ec1f27
f37022
9bcb3c

Requirements
Must have
• Colorful pictures nature, brings out emotion, colorful, children from various parts of the world, animals.
• Tried to down load some pictures but would not go thru.

```html
<!DOCTYPE html>
<html lang="en">
<head>
<meta charset="utf-8">
<title>Bright Meadow Foundation</title>
<link rel="stylesheet" href="https://fonts.googleapis.com/css2?family=Montserrat:wght@400;500;600;700;800&display=swap">
<style>
:root{
  --orange:#f37022;
  --orange-2:#f68b2e;
  --green:#7fd321;
  --green-dark:#5fae13;
  --purple:#876aae;
  --ink:#1e1e1e;
  --text:#333;
  --muted:#555;
  --white:#fff;
  --footer-bg:#f7f7f7;
}
*{box-sizing:border-box;margin:0;padding:0}
html,body{width:1200px;height:3870px;overflow:hidden}
body{position:relative;font-family:'Montserrat',sans-serif;color:var(--text);background:var(--white)}
.abs{position:absolute}

/* nav */
.site-nav{left:0;top:0;width:1200px;height:92px;background:var(--white)}
.brand{left:89px;top:24px;display:flex;align-items:center;gap:8px}
.brand-dot{width:22px;height:22px;border-radius:50%;background:var(--purple)}
.brand-name{font-size:13px;font-weight:600;color:var(--purple)}
.nav-links{left:334px;top:34px;display:flex;gap:44px;font-size:15px;font-weight:500;color:var(--ink)}
.nav-links .active{color:var(--orange);border-bottom:2px solid var(--orange);padding-bottom:6px}
.btn{display:inline-flex;align-items:center;justify-content:center;background:var(--orange);color:var(--white);font-weight:600;border-radius:5px}
.nav-donate{left:967px;top:27px;width:146px;height:36px;font-size:15px}

/* hero */
.hero-photo{left:0;top:92px;width:1200px;height:581px;background:linear-gradient(120deg,#5b544c 0%,#8b7d6d 35%,#b7a58e 60%,#6f6258 100%)}
.mission{left:92px;top:150px;width:470px;height:430px;border-radius:60px 60px 200px 200px;background:linear-gradient(180deg,#8ae02a,var(--green));border:7px solid var(--orange);padding:70px 48px 0;text-align:center;color:var(--white)}
.mission h1{font-size:28px;font-weight:700;margin-bottom:18px}
.mission p{font-size:14.5px;line-height:1.45}
.hero-dots{left:565px;top:648px;display:flex;gap:8px}
.hero-dots span{width:12px;height:8px;border-radius:4px;background:var(--white)}
.hero-dots .on{width:34px;background:var(--orange)}

/* light section */
.wash{left:0;top:673px;width:1200px;height:1518px;background:radial-gradient(circle at 15% 40%,#e9f3fb 0,transparent 30%),radial-gradient(circle at 85% 25%,#f9e6d4 0,transparent 28%),radial-gradient(circle at 50% 70%,#e4eff9 0,transparent 35%),radial-gradient(circle at 10% 85%,#fde8ea 0,transparent 25%),#fcfdfe}
.section-title{font-size:26px;font-weight:700;color:var(--orange)}
.about-title{left:89px;top:772px}
.about-text{left:89px;top:818px;width:1024px;font-size:14.5px;line-height:1.6;color:var(--ink)}
.more-link{font-size:18px;font-weight:600;color:var(--orange)}
.read-more{left:968px;top:986px}
.team-title{left:89px;top:1022px}

.team-card{top:1070px;width:247px;height:191px;border-radius:8px;background:linear-gradient(135deg,var(--orange),var(--orange-2));color:var(--white);text-align:center}
.team-card.featured{background:linear-gradient(135deg,#e88a50,#ec9f6a)}
.socials{display:flex;justify-content:center;gap:22px;margin-top:34px}
.socials span{width:30px;height:30px;border-radius:50%;border:2px solid var(--white)}
.team-card .blurb{font-size:14px;line-height:1.45;padding:22px 40px 0}
.avatar{width:72px;height:72px;border-radius:50%;margin:26px auto 0;background:radial-gradient(circle,#c98a6a,#5a3a2c)}
.team-card h3{font-size:21px;font-weight:700;margin-top:18px}
.team-card .role{font-size:15px;font-weight:600;margin-top:20px}

.projects-title{left:0;top:1414px;width:1200px;text-align:center;font-size:27px;font-weight:700;color:var(--ink)}
.projects-text{left:170px;top:1457px;width:860px;text-align:center;font-size:14.5px;line-height:1.45;color:var(--ink)}

.project-card{top:1552px;width:334px;height:460px;background:var(--white);border-radius:8px;box-shadow:0 4px 16px rgba(0,0,0,.14);overflow:hidden}
.project-photo{height:194px}
.stats{display:flex;justify-content:space-between;padding:12px 20px 0;font-size:15px;font-weight:700;color:var(--ink)}
.stats b{color:var(--orange)}
.bar{margin:10px 20px 0;height:10px;border-radius:5px;border:1px solid #d9d9d9;background:#f1f1f1;overflow:hidden}
.bar i{display:block;height:100%;background:var(--orange)}
.percent{text-align:center;font-size:15px;font-weight:700;color:var(--orange);margin-top:10px}
.project-card h3{text-align:center;font-size:24px;font-weight:700;color:var(--ink);margin-top:8px}
.project-card p{text-align:center;font-size:14px;line-height:1.45;color:var(--muted);padding:8px 32px 0}
.card-donate{top:2023px;width:146px;height:34px;font-size:14px}
.show-more{left:0;top:2078px;width:1200px;text-align:center}

/* impact band */
.impact{left:0;top:2191px;width:1200px;height:382px;background:linear-gradient(90deg,var(--orange),var(--orange-2) 60%,#f9a350)}
.impact-text{left:89px;top:2300px;width:400px;font-size:27px;font-weight:700;line-height:1.22;color:var(--white)}
.join{left:89px;top:2459px;width:146px;height:36px;background:var(--white);color:var(--orange);border-radius:5px;font-size:14px;font-weight:600;display:flex;align-items:center;justify-content:center}
.stat{top:2278px;width:220px;text-align:center;color:var(--white)}
.stat-icon{width:154px;height:154px;border-radius:50%;margin:0 auto;border:4px solid var(--purple)}
.stat .num{font-size:15px;font-weight:700;color:var(--purple);margin-top:8px;line-height:1.2}
.stat .label{font-size:19px;font-weight:600;line-height:1.3}

/* contact */
.contact-photo{left:0;top:2573px;width:1200px;height:859px;background:linear-gradient(110deg,#3a3530,#6d6356 45%,#4a4640 75%,#2f2b27)}
.contact-title{left:89px;top:2745px;font-size:50px;font-weight:800;color:var(--orange)}
.contact-sub{left:89px;top:2840px;font-size:33px;font-weight:700;line-height:1.3;color:var(--white)}
.contact-sub em{font-style:normal;color:var(--orange)}
.field{left:701px;width:410px;background:var(--white);border:2px solid var(--orange);border-radius:5px;padding:16px;font-size:18px;color:#444}
.send{left:968px;top:3251px;width:144px;height:36px;font-size:17px}

/* footer */
.footer{left:0;top:3432px;width:1200px;height:357px;background:var(--footer-bg)}
.foot-brand{left:89px;top:3478px}
.contact-line{left:89px;display:flex;align-items:flex-start;gap:14px;font-size:18px;font-weight:600;color:var(--purple);line-height:1.3}
.pin{width:28px;height:28px;border-radius:50%;background:#e8e8ee;flex:none;display:flex;align-items:center;justify-content:center}
.foot-socials{left:89px;top:3680px;display:flex;gap:18px}
.foot-socials span{width:50px;height:50px;border-radius:50%;background:#ececec}
.foot-col{top:3490px}
.foot-col h4{font-size:22px;font-weight:700;color:var(--orange);margin-bottom:26px}
.foot-col li{list-style:none;font-size:18px;color:var(--ink);line-height:37px}
.copyright{left:0;top:3789px;width:1200px;height:81px;background:var(--orange);color:var(--white);font-size:12px;display:flex;align-items:center;justify-content:center}
</style>
</head>
<body>

<header class="abs site-nav">
  <div class="abs brand"><span class="brand-dot"></span><span class="brand-name">Bright Meadow</span></div>
  <nav class="abs nav-links"><span class="active">Home</span><span>About Us</span><span>Projects</span><span>Get Involved</span><span>Contact Us</span></nav>
  <span class="abs btn nav-donate">Donate</span>
</header>

<section>
  <div class="abs hero-photo" role="img" aria-label="Smiling schoolchildren in uniforms waving on a village street"></div>
  <div class="abs mission">
    <h1>Mission Statement</h1>
    <p>Aliquam faucibus, odio nec commodo aliquam, neque felis placerat dui, a porta ante lectus dapibus est. Aliquam a bibendum mi, sed condimentum est. Mauris arcu odio, vestibulum quis dapibus sit amet, finibus id turpis. Aliquam semper fringilla semper. Sed nec velit sit amet dolor pulvinar feugiat, interdum egestas, nibh ex maximus arcu, non posuere sem nulla in augue.</p>
  </div>
  <div class="abs hero-dots"><span class="on"></span><span></span><span></span></div>
</section>

<div class="abs wash" role="img" aria-label="Soft pastel background of colourful painted handprints"></div>

<section>
  <h2 class="abs section-title about-title">About Us</h2>
  <p class="abs about-text">Aliquam faucibus, odio nec commodo aliquam, neque felis placerat dui, a port ante lectus dapibus est. Aliquam a bibendum mi, sed condimentum est. Mauris arcu odio, vestibulum quis dapibus sit amet, finibus id turpis. Aliquam semper fringilla semper. Sed nec velit sit amet dolor pulvinar feugiat. Suspendisse blandit, nulla sed interdum egestas, nibh ex maximus arcu, non posuere sem nulla in augue. Class aptent taciti sociosqu ad litora torquent per conubia nostra, per inceptos himenaeos. Maecenas mattis sapien vel sollicitudin blandit. Donec nec porttitor eros. Praesent blandit, erat non vehicula rutrum, mauris orci scelerisque urna, rutrum malesuada odio magna at felis. Fusce convallis elit in risus tincidunt ullamcorper. Aliquam maximus dolor turpis, nec commodo libero mattis</p>
  <span class="abs more-link read-more">Read More &#187;</span>

  <h2 class="abs section-title team-title">Our Team</h2>
  <div class="abs team-card featured" style="left:89px">
    <div class="socials"><span></span><span></span><span></span><span></span></div>
    <p class="blurb">Cras eu est congue, placerat dui ut, tincidunt nisi. Nulla leo elit,</p>
  </div>
  <div class="abs team-card" style="left:347px">
    <div class="avatar" role="img" aria-label="Portrait of Rosa Tembley"></div>
    <h3>Rosa Tembley</h3><div class="role">FNP</div>
  </div>
  <div class="abs team-card" style="left:606px">
    <div class="avatar" role="img" aria-label="Portrait of Dorla Penn"></div>
    <h3>Dorla Penn</h3><div class="role">FNP</div>
  </div>
  <div class="abs team-card" style="left:866px">
    <div class="avatar" role="img" aria-label="Portrait of Wade Marlow" style="background:radial-gradient(circle,#a66bd8,#3c2a7a)"></div>
    <h3>Wade Marlow</h3><div class="role">FNP</div>
  </div>
</section>

<section>
  <h2 class="abs projects-title">Projects</h2>
  <p class="abs projects-text">Duis pretium gravida enim, vel maximus ligula fermentum a. Sed rhoncus eget ex id egestas. Nam nec nisl placerat, tempus erat a, condimentum metus. Curabitur nulla nisi, lacinia at lobortis at, suscipit at nibh. Proin quis lectus finibus, mollis purus vitae, rutrum neque. Pellentesque habitant morbi tristique senectus</p>

  <article class="abs project-card" style="left:89px">
    <div class="project-photo" role="img" aria-label="Woman in a knitted hat and gloves outdoors" style="background:linear-gradient(135deg,#6b5048,#b4807a 50%,#d4a8a8)"></div>
    <div class="stats"><span>Raised: <b>$9000</b></span><span>Goal: <b>$10000</b></span></div>
    <div class="bar"><i style="width:50%"></i></div>
    <div class="percent">50%</div>
    <h3>Columbia Disaster</h3>
    <p>Duis pretium gravida enim, vel maximus ligula fermentum a. Sed rhoncus eget ex id egestas. Nam nec nisl placerat, tempus erat a, condimentum metus. Curabitur nulla</p>
  </article>
  <article class="abs project-card" style="left:433px">
    <div class="project-photo" role="img" aria-label="Elderly woman seated on a cobbled village street" style="background:linear-gradient(135deg,#8a7a66,#b5a48a 50%,#5d5145)"></div>
    <div class="stats"><span>Raised: <b>$9000</b></span><span>Goal: <b>$10000</b></span></div>
    <div class="bar"><i style="width:25%"></i></div>
    <div class="percent">25%</div>
    <h3>Venezuela Hunger</h3>
    <p>Duis pretium gravida enim, vel maximus ligula fermentum a. Sed rhoncus eget ex id egestas. Nam nec nisl placerat, tempus erat a, condimentum metus. Curabitur nulla</p>
  </article>
  <article class="abs project-card" style="left:777px">
    <div class="project-photo" role="img" aria-label="Child with arms raised over head in a colourful shirt" style="background:linear-gradient(135deg,#e07a2e,#5a3a2a 50%,#b33a6a)"></div>
    <div class="stats"><span>Raised: <b>$5000</b></span><span>Goal: <b>$10000</b></span></div>
    <div class="bar"><i style="width:90%"></i></div>
    <div class="percent">90%</div>
    <h3>Columbia Education</h3>
    <p>Duis pretium gravida enim, vel maximus ligula fermentum a. Sed rhoncus eget ex id egestas. Nam nec nisl placerat, tempus erat a, condimentum metus. Curabitur nulla</p>
  </article>
  <span class="abs btn card-donate" style="left:183px">Donate Now</span>
  <span class="abs btn card-donate" style="left:527px">Donate Now</span>
  <span class="abs btn card-donate" style="left:871px">Donate Now</span>
  <div class="abs more-link show-more">Show more Projects &#187;</div>
</section>

<section class="abs impact"></section>
<p class="abs impact-text">We are serving humanity since 25 years to people with trust and we are happy.</p>
<span class="abs join">Join Us</span>
<div class="abs stat" style="left:489px">
  <div class="stat-icon" role="img" aria-label="Heart held in an open hand" style="background:radial-gradient(circle,#9fe04a,var(--green-dark))"></div>
  <div class="num">$89,952</div><div class="label">Donations</div>
</div>
<div class="abs stat" style="left:705px">
  <div class="stat-icon" role="img" aria-label="Group of volunteers standing together" style="background:radial-gradient(circle,#b7e6f5,#6cc0de)"></div>
  <div class="num">952</div><div class="label">Volunteers</div>
</div>
<div class="abs stat" style="left:930px">
  <div class="stat-icon" role="img" aria-label="Family held in caring hands" style="background:radial-gradient(circle,#b7e6f5,#6cc0de)"></div>
  <div class="num">24hrs</div><div class="label">Corporate Support</div>
</div>

<section>
  <div class="abs contact-photo" role="img" aria-label="Child looking through a chain-link fence, with a warm orange tint on the left"></div>
  <h2 class="abs contact-title">CONTACT US</h2>
  <p class="abs contact-sub">They <em>NEED</em><br>your help....</p>
  <div class="abs field" style="top:2747px;height:61px">Enter Your Name</div>
  <div class="abs field" style="top:2823px;height:61px">Enter Your Email</div>
  <div class="abs field" style="top:2900px;height:331px">Enter Your Message</div>
  <span class="abs btn send">Send</span>
</section>

<footer class="abs footer"></footer>
<div class="abs brand foot-brand"><span class="brand-dot"></span><span class="brand-name">Bright Meadow</span></div>
<div class="abs contact-line" style="top:3552px">
  <span class="pin"><svg width="14" height="14" viewBox="0 0 24 24"><path fill="#876aae" d="M6.6 10.8a15 15 0 0 0 6.6 6.6l2.2-2.2a1 1 0 0 1 1-.3 11 11 0 0 0 3.6.6 1 1 0 0 1 1 1V20a1 1 0 0 1-1 1A17 17 0 0 1 3 4a1 1 0 0 1 1-1h3.5a1 1 0 0 1 1 1c0 1.2.2 2.5.6 3.6a1 1 0 0 1-.3 1z"/></svg></span>
  <span>(555)014-7732</span>
</div>
<div class="abs contact-line" style="top:3594px">
  <span class="pin"><svg width="14" height="14" viewBox="0 0 24 24"><path fill="#876aae" d="M12 2a7 7 0 0 0-7 7c0 5 7 13 7 13s7-8 7-13a7 7 0 0 0-7-7zm0 9.5A2.5 2.5 0 1 1 12 6.5a2.5 2.5 0 0 1 0 5z"/></svg></span>
  <span>48 Orchard Lane, 3rd Floor<br>Linden Vale</span>
</div>
<div class="abs foot-socials"><span></span><span></span><span></span><span></span></div>

<div class="abs foot-col" style="left:433px"><h4>Get Involved</h4><ul><li>Donate</li><li>Account</li><li>Employer Center</li><li>Projects</li><li>Projects</li></ul></div>
<div class="abs foot-col" style="left:683px"><h4>Community</h4><ul><li>Help/Contact Us</li><li>About Us</li><li>Blog</li><li>Guides</li><li>Guides</li></ul></div>
<div class="abs foot-col" style="left:938px"><h4>Work With Us</h4><ul><li>Research</li><li>Location</li><li>Advertisers</li><li>Careers</li><li>Careers</li></ul></div>

<div class="abs copyright">Copyrights &#169; 2019 - BRIGHT MEADOW FOUNDATION</div>

</body>
</html>
```